Landing Page Design für Immobilienbüro
Zielgruppe
Wir sind ein regionales Immobilienbüro, spezialisiert auf den Verkauf bzw. die Vermittlung von Immobilien, vorwiegend im Bereich der Wohnimmobilien.
Wir wollen unseren Bekanntheitsgrad zunächst in der Region und zukünftig auch regionsübergreifend erweitern, stärken und dauerhaft Marktanteile sichern.
Hierzu möchten wir zielgruppenorientierte Landingpages einsetzen, welche auch via Plaxo-Ads etc. beworben werden und suchmaschinenfreundlich gestaltet sind soll. Hier ist also neben der kreativen Fachkenntnis auch Kenntnis in SEO etc. gefragt.
Auch könnten wir uns eine dauerhafte, auch auf Erfolg basierte Zusammenarbeit vorstellen.
Zielgruppen für die Landingpage:
Personen, welche eine Immobilie geerbt haben
Personen, deren Immobilie zu groß / zu klein ist
Personen, die sich trennen und die Immobilie deswegen verkauft werden muss
Aufgabenstellung
Die Landingpage soll jeweils an unser CI (siehe haus-lotsen.immo) angepasst sein, so dass der Wiedererkennungswert steigt. Die Seite soll die Möglichkeit eines Kontaktformulars, eines Videos, Einbindung von Kundenmeinungen etc. beinhalten.

```html
<!DOCTYPE html>
<html lang="de">
<head>
<meta charset="utf-8">
<title>haus-lotsen.immo – Haus verkaufen</title>
<link href="https://fonts.googleapis.com/css2?family=Roboto:wght@300;400;500;700;900&display=swap" rel="stylesheet">
<style>
:root{
  --green:#7fba2a;
  --blue:#1a86c8;
  --blue-deep:#0b7ec4;
  --ink:#2b2b2b;
  --muted:#555;
  --field:#ececec;
  --white:#fff;
}
*{box-sizing:border-box;margin:0;padding:0}
html,body{width:1200px;height:4174px;overflow:hidden}
body{position:relative;font-family:'Roboto',sans-serif;color:var(--ink);background:var(--white)}
.abs{position:absolute}
/* header */
.site-header{left:0;top:0;width:1200px;height:78px;background:var(--white)}
.brand{left:66px;top:24px;display:flex;align-items:center;gap:8px;font-size:22px;font-weight:700;color:var(--green)}
.brand-mark{width:18px;height:18px;background:var(--blue)}
.nav a{position:absolute;top:34px;font-size:9px;font-weight:500;color:var(--ink);text-decoration:none;letter-spacing:.3px}
.nav .contact{top:27px;left:1062px;width:71px;height:25px;border:2px solid var(--green);color:var(--green);display:flex;align-items:center;justify-content:center}
/* hero */
.hero{left:0;top:78px;width:1200px;height:647px;background:linear-gradient(120deg,#d9d4cc 0%,#c9bfb1 40%,#e6e2dc 70%,#cfc3b2 100%)}
.hero h1{left:66px;top:320px;font-size:48px;line-height:53px;font-weight:900;color:var(--white);text-transform:uppercase}
.hero-input{left:66px;top:523px;width:433px;height:53px;background:var(--white);font-size:12px;color:#888;padding-left:34px;display:flex;align-items:center}
.btn{background:var(--green);color:var(--white);display:flex;align-items:center;justify-content:center;font-size:13px}
.hero-btn{left:499px;top:523px;width:176px;height:53px}
/* intro */
.kicker{font-size:15px;color:var(--blue)}
.intro-kicker{left:66px;top:814px}
.intro-title{left:66px;top:838px;font-size:22px;font-weight:700;color:var(--green)}
.intro-text{left:66px;top:881px;width:440px;font-size:12px;line-height:19px;color:#888}
.step-img{top:997px;width:265px;height:178px}
.step-label{top:1206px;font-size:8px;font-weight:700;color:var(--blue)}
.step-title{top:1222px;font-size:16px;line-height:24px;font-weight:700;color:var(--green);width:240px}
.step-text{top:1298px;font-size:12px;line-height:19px;color:var(--muted);width:260px}
/* stats */
.stats{left:0;top:1488px;width:1200px;height:235px;background:linear-gradient(180deg,rgba(26,134,200,.92),rgba(20,120,190,.95)),linear-gradient(90deg,#6aa,#8bc)}
.stats-num{left:0;width:1200px;top:1508px;text-align:center;font-size:52px;font-weight:900;color:var(--white)}
.stats-label{left:0;width:1200px;top:1592px;text-align:center;font-size:12px;color:var(--white)}
.stats-btn{left:492px;top:1632px;width:217px;height:58px}
/* faq */
.faq-photo{left:0;top:1723px;width:445px;height:671px;background:linear-gradient(160deg,#eef0f2,#cdb79b 60%,#b89a78)}
.faq-title{left:505px;top:1816px;font-size:28px;font-weight:500}
.faq-title span{color:var(--green)}
.faq-item{left:507px;width:626px;height:47px;border:1px solid #e1e1e1;font-size:12px;font-weight:500;padding-left:38px;display:flex;align-items:center}
.faq-item::after{content:"+";position:absolute;right:40px;top:8px;font-size:24px;color:var(--blue)}
.faq-open{left:507px;top:2186px;width:626px;height:208px;background:var(--green);color:var(--white);padding:30px 90px 0 38px}
.faq-open h3{font-size:12px;font-weight:500;margin-bottom:12px}
.faq-open p{font-size:9.5px;line-height:24px}
.faq-open::after{content:"–";position:absolute;right:40px;top:24px;font-size:14px}
/* video */
.video-kicker{left:70px;top:2651px;font-size:20px;font-weight:300;color:#444}
.video-title{left:70px;top:2680px;font-size:27px;font-weight:700;color:var(--blue)}
.video-text{left:70px;top:2745px;width:300px;font-size:12px;line-height:24px;color:var(--muted)}
.video-back{left:578px;top:2713px;width:319px;height:224px;background:var(--blue)}
.video-frame{left:605px;top:2582px;width:527px;height:327px;background:linear-gradient(180deg,#a9c3de 0%,#dbe5ee 55%,#9aa28c 85%,#7b8466 100%)}
.play{left:829px;top:2707px;width:80px;height:80px;border-radius:50%;background:var(--green)}
/* testimonial */
.person{left:13px;top:3065px;width:405px;height:503px;background:linear-gradient(180deg,#f5f5f5,#e8e8e8 40%,#2d3340 45%,#222833 100%)}
.quote-title{left:492px;top:3172px;font-size:45px;font-weight:300;color:var(--ink)}
.quote-title b{font-weight:700;color:var(--blue)}
.quote-text{left:494px;top:3257px;width:560px;font-size:12px;line-height:24px;color:var(--muted)}
.quote-name{left:494px;top:3348px;font-size:12px;font-weight:700;color:var(--green)}
/* footer */
.footer{left:0;top:3568px;width:1200px;height:606px;background:var(--blue-deep)}
.footer-strip{left:798px;top:3568px;width:162px;height:606px;background:var(--green)}
.footer-brand{left:66px;top:3660px;display:flex;align-items:center;gap:10px;font-size:32px;font-weight:700;color:var(--white)}
.footer-brand i{width:26px;height:26px;background:var(--white);display:block}
.info{left:66px;color:var(--white);font-size:12px;line-height:19px}
.info b{font-weight:700}
.social{left:66px;top:3983px;display:flex;gap:14px}
.social i{width:15px;height:15px;border-radius:50%;background:var(--white);display:block}
.form{left:623px;top:3644px;width:510px;height:452px;background:var(--white)}
.form h2{position:absolute;left:49px;top:50px;font-size:20px;font-weight:500}
.field{left:672px;width:414px;background:var(--field);font-size:12px;color:#555;padding:14px 35px}
.send{left:672px;top:4001px;width:414px;height:45px}
</style>
</head>
<body>
<header class="site-header abs">
  <div class="brand abs"><span class="brand-mark"></span>haus-lotsen.immo</div>
  <nav class="nav">
    <a style="left:771px">LEISTUNGEN</a>
    <a style="left:865px">ÜBER UNS</a>
    <a style="left:947px">AKTUELLE ANGEBOTE</a>
    <a class="contact">KONTAKT</a>
  </nav>
</header>

<section class="hero abs" role="img" aria-label="Junge Familie sitzt zwischen Umzugskartons unter einem Dach aus Karton"></section>
<h1 class="abs hero h1" style="left:66px;top:320px;font-size:48px;line-height:53px;font-weight:900;color:#fff;background:none;width:auto;height:auto">Fertig,<br>eingestellt,<br>verkauft.</h1>
<div class="hero-input abs">Geben Sie Ihre Adresse ein</div>
<div class="btn hero-btn abs">Angebot bekommen</div>

<p class="kicker intro-kicker abs">Verkaufen Sie Ihr Haus.</p>
<h2 class="intro-title abs">Überspringen Sie die harten Teile.</h2>
<p class="intro-text abs">So vermeiden wir unnötige Schritte, um den Verkauf Ihres Hauses einfach, schnell und stressfrei zu gestalten.</p>

<div class="step-img abs" style="left:65px;background:linear-gradient(135deg,#5b7891,#c7d3dc)" role="img" aria-label="Hand hält ein Tablet mit der Angebotsseite"></div>
<div class="step-label abs" style="left:65px">SCHRITT 1</div>
<h3 class="step-title abs" style="left:65px">Holen Sie sich in wenigen Minuten ein Angebot</h3>
<p class="step-text abs" style="left:65px">Sehen Sie sich in wenigen Schritten Ihr vorläufiges Angebot an</p>

<div class="step-img abs" style="left:471px;background:linear-gradient(135deg,#3a3a3a,#e9e9e9 60%,#7a5a45)" role="img" aria-label="Videoaufnahme eines modernen Wohnzimmers"></div>
<div class="step-label abs" style="left:471px">SCHRITT 2</div>
<h3 class="step-title abs" style="left:471px">Machen Sie eine Video-Anleitung</h3>
<p class="step-text abs" style="left:471px">Zeigen Sie uns Ihr Zuhause, damit wir unser bestes Angebot machen können.</p>

<div class="step-img abs" style="left:869px;background:linear-gradient(135deg,#2f3a4c,#dfe8ea 60%,#f3f3f3)" role="img" aria-label="Übergabe eines Hausschlüssels"></div>
<div class="step-label abs" style="left:869px">SCHRITT 3</div>
<h3 class="step-title abs" style="left:869px">Schließen Sie und umziehen, stressfrei</h3>
<p class="step-text abs" style="left:869px">Wählen Sie aus, wann Sie schließen möchten. Erhalten Sie innerhalb von Tagen bezahlt.</p>

<section class="stats abs" role="img" aria-label="Modernes Haus unter blauem Farbschleier"></section>
<div class="stats-num abs">1,000 +</div>
<div class="stats-label abs">ANGEBOTE ANGEFORDERT</div>
<div class="btn stats-btn abs">Angebot bekommen</div>

<div class="faq-photo abs" role="img" aria-label="Paar trägt Umzugskartons in einer hellen Wohnung"></div>
<h2 class="faq-title abs">Häufig <span>Gestellte Fragen!</span></h2>
<div class="faq-item abs" style="top:1910px">Vestibulum tristique mauris in elit ultrices?</div>
<div class="faq-item abs" style="top:1978px">Vivamus consequat fermentum neque nec finibus?</div>
<div class="faq-item abs" style="top:2048px">Sed viverra, libero ut sollicitudin finibus?</div>
<div class="faq-item abs" style="top:2116px">Donec justo quam, aliquam suscipit tellus nec, lobortis vehicula lorem?</div>
<div class="faq-open abs">
  <h3>Vivamus arcu magna, vehicula nec viverra nec, consequat non mi?</h3>
  <p>Sed finibus urna ut magna aliquet bibendum. Aenean blandit nisl neque, id aliquet tellus viverra sed.<br>Fusce rutrum ornare arcu ut placerat. Mauris id purus et nunc aliquam finibus ac vitae nulla.</p>
  <p style="margin-top:24px">Nam gravida ipsum sit amet libero fermentum, vitae congue ipsum congue. Quisque aliquam eleifend est et aliquet.</p>
</div>

<p class="video-kicker abs">Verkaufen Sie Ihr Haus?</p>
<h2 class="video-title abs">Wir machen das einfach.</h2>
<p class="video-text abs">Wir helfen Ihnen, Ihr Haus zu Ihren Bedingungen zu verkaufen und dabei Tausende zu sparen.</p>
<div class="video-back abs"></div>
<div class="video-frame abs" role="img" aria-label="Video: modernes Einfamilienhaus unter bewölktem Himmel"></div>
<div class="play abs"><svg width="80" height="80" viewBox="0 0 80 80"><path d="M33 27 L53 40 L33 53 Z" fill="#fff"/></svg></div>

<div class="person abs" role="img" aria-label="Porträt eines Kunden im Sakko mit verschränkten Armen"></div>
<h2 class="quote-title abs"><b>Kunden</b> empfehlen uns</h2>
<p class="quote-text abs">Curabitur quis tincidunt turpis. Morbi tincidunt, nisl vel hendrerit rutrum, leo massa vehicula mi, non facilisis tortor mi in ex. Nullam vitae dapibus turpis, sed commodo erat. Ut venenatis pretium tempus. Integer scelerisque lacus at felis congue, suscipit mollis mi volutpat.</p>
<p class="quote-name abs">Jonas Berger</p>
<svg class="abs" style="left:990px;top:3349px" width="44" height="14" viewBox="0 0 44 14"><path d="M9 2 L4 7 L9 12" stroke="#ccc" stroke-width="1.6" fill="none"/><path d="M35 2 L40 7 L35 12" stroke="#1a86c8" stroke-width="1.6" fill="none"/></svg>

<footer class="footer abs"></footer>
<div class="footer-strip abs"></div>
<div class="footer-brand abs"><i></i>haus-lotsen.immo</div>
<p class="info abs" style="top:3772px">Mail<br><b>info@haus-lotsen.de</b></p>
<p class="info abs" style="top:3828px">Telefon<br><b>030412 77 19</b></p>
<p class="info abs" style="top:3884px">Adresse<br><b>Lindenweg 12<br>37120 Bovenden</b></p>
<p class="info abs" style="top:3958px">Sozialen Medien</p>
<div class="social abs"><i></i><i></i><i></i></div>
<div class="form abs"><h2>Haben Sie eine Nachricht?</h2></div>
<div class="field abs" style="top:3746px;height:45px">Name</div>
<div class="field abs" style="top:3811px;height:46px">E-Mail</div>
<div class="field abs" style="top:3876px;height:102px">Nachricht</div>
<div class="btn send abs">Senden</div>
</body>
</html>
```